Menu Design marlowe

I need to create a take out menu for my restaurant something nice with some pictures. clean and simple with the colors of my reatsurant. which are orange and black. mostly black.

its fairly simple it has to be 4 pages front cover, inside front menu then 2nd page front and back with menu then 3rd page back front menu, back 3rd sushi menu with specials. final page 4th page, back map with adress and opening hours. and back cover final.

simple elegant and class. black and orange i will send logo and menu as well and pictures.

i am a high end bistro that serves gourmet pizza and pasta. we also have a sushi bar.
the menu will be 6 inches width by 9 inches

the menu that i sent is a pdf file. had an error with word please change font and make a new word dosument.

thank you

Industry/Entity Type

Restaurant

Requirements
Must have
• the colors which are black and orange. mostly black.

```html
<!DOCTYPE html>
<html lang="fr">
<head>
<meta charset="utf-8">
<title>Marlowe Bistro – Menu</title>
<link rel="stylesheet" href="https://fonts.googleapis.com/css2?family=PT+Sans:wght@400;700&display=swap">
<style>
  :root{
    --sheet:#f3bd78;
    --ink:#000;
    --paper:#fff;
    --white:#fff;
    --orange:#f6b64f;
    --photo-dark:#3a3a3a;
    --photo-mid:#8d8d8d;
    --photo-light:#d9d9d9;
  }
  *{margin:0;padding:0;box-sizing:border-box}
  html,body{width:1200px;height:848px;overflow:hidden;background:var(--sheet)}
  body{position:relative;font-family:"PT Sans",Arial,sans-serif;font-size:11px;line-height:14.6px;letter-spacing:-0.15px;text-transform:uppercase}
  .page{position:absolute;top:16px;height:818px;background:var(--paper)}
  .page-left{left:18px;width:566px}
  .page-right{left:613px;width:572px}
  .menu-column{position:absolute;top:0;height:100%;background:var(--ink)}
  .page-left .menu-column{left:0;width:322px}
  .page-right .menu-column{left:255px;width:317px}
  .photo-strip{position:absolute;top:0;height:100%;display:flex;flex-direction:column}
  .page-left .photo-strip{left:322px;width:244px}
  .page-right .photo-strip{left:0;width:255px}
  .photo{flex:1;border-bottom:2px solid var(--paper)}
  .photo:last-child{border-bottom:0}
  .photo.a{background:linear-gradient(160deg,var(--photo-light),var(--photo-mid) 60%,var(--photo-dark))}
  .photo.b{background:linear-gradient(200deg,var(--photo-dark),var(--photo-mid) 55%,var(--photo-light))}
  .photo.c{background:linear-gradient(135deg,var(--photo-mid),var(--photo-light) 50%,var(--photo-mid))}
  .section-title{position:absolute;color:var(--white);font-size:14px;font-weight:700;letter-spacing:.2px}
  .item{position:absolute;color:var(--orange);white-space:nowrap}
  .page-left .item{left:12px;width:300px}
  .page-right .item{left:3px;width:310px}
  .name{color:var(--white)}
  .price{position:absolute;top:0;color:var(--white);text-transform:none}
  .page-left .price{left:271px}
  .page-right .price{left:278px}
  .white{color:var(--white)}
</style>
</head>
<body>

<section class="page page-left">
  <div class="menu-column">
    <h2 class="section-title" style="left:125px;top:6px">PIZZA</h2>

    <div class="item" style="top:38px"><div class="name">Margarita</div><div>Sauce tomate, mozzarella &amp; basilic</div><span class="price">$15.50</span></div>
    <div class="item" style="top:81px"><div class="name">Champignon</div><div>Champignon, sauce tomate, mozzarella</div><span class="price">$17.50</span></div>
    <div class="item" style="top:124px"><div class="name">Trilogie d'olive / olive trilogy</div><div>Olives, sauce tomate piquante &amp;mozzarella<br>Olives, spicy tomato sauce &amp;mozzarella</div><span class="price">$17.50</span></div>
    <div class="item" style="top:182px"><div class="name">Vegetarienne / vegetarien</div><div>Legumes grilles sauce tomato &amp;mozzarella<br>Grilled veggies tomato sauce, mozzarella</div><span class="price">$18.50</span></div>
    <div class="item" style="top:241px"><div class="name">Pizza Marlowe / Marlowe pizza</div><div>Tomates, sechees, aubergine, olives, sauce,<br>tomate&amp; mozzarella<br>Sun dried tomatoes, eggplant, olives,<br>tomato sauce &amp; mozzarella</div><span class="price">$18.50</span></div>
    <div class="item" style="top:328px"><div class="name">Grecque/Greek</div><div>Feta, olives, oignons rouges, mozzarella,<br>sauce tomate<br>Feta, olives, red onions, mozzarella tomato<br>sauce</div><span class="price" style="left:269px">$19.00</span></div>
    <div class="item" style="top:415px"><div class="name">Thon/Tuna</div><div>Thon, olives, sauce tomate &amp; mozzarella<br>Tuna, olives, tomato sauce &amp; mozzarella</div><span class="price">$18.50</span></div>
    <div class="item" style="top:473px"><div class="name">Nicoise</div><div>Anchois, olives, sauce tomate &amp; mozzarella<br>Anchovies, olives mozzarella &amp; tomato<br>sauce</div><span class="price" style="left:269px">$19.00</span></div>
    <div class="item" style="top:546px"><div class="name">Fruit de mar / seafood</div><div>Crevettes, poireaux, sauce tomate &amp; mozza-<br>rella<br>Shrimp, leeks, tomato sauce &amp; mozzarella</div><span class="price" style="left:269px">$19.00</span></div>
    <div class="item" style="top:619px"><div class="name" style="font-weight:700">Calzon</div><div>Poivron rouge, vert &amp; jaune, champignons,<br>oignons<br>Sauce tomate &amp; mozzarella<br>Red, yellow &amp; green peppers, mushrooms,<br>onions tomato sauce &amp; mozzarella</div><span class="price">$18.50</span></div>
    <div class="item white" style="top:720px;font-size:10.5px">Toutes nos pizzas sont disponibles sans fromage<br>All our pizzas are avaialble without cheese<br>Ajoutez deux oeufs / add two eggs<br>Pate ble entier
      <span class="price" style="top:29px;left:279px">$1.95</span><span class="price" style="top:44px;left:279px">$1.25</span></div>
  </div>
  <div class="photo-strip">
    <div class="photo a" role="img" aria-label="Bistro storefront on a tree-lined street"></div>
    <div class="photo b" role="img" aria-label="Bistro awning with name and street number"></div>
    <div class="photo c" role="img" aria-label="Blurred plants in front of the bistro sign"></div>
    <div class="photo a" role="img" aria-label="Pastry shop window lettering seen through grass"></div>
    <div class="photo b" role="img" aria-label="Bistro interior with counter and staff"></div>
  </div>
</section>

<section class="page page-right">
  <div class="photo-strip">
    <div class="photo c" role="img" aria-label="Dining room with tables and guests"></div>
    <div class="photo a" role="img" aria-label="Bright dining room with large windows"></div>
    <div class="photo b" role="img" aria-label="Table set with water glasses"></div>
    <div class="photo c" role="img" aria-label="Dining room seen from the entrance"></div>
    <div class="photo a" role="img" aria-label="Server carrying plates in the dining room"></div>
  </div>
  <div class="menu-column">
    <h2 class="section-title" style="left:3px;top:7px">ENTREES / APPETIZERS</h2>

    <div class="item" style="top:38px"><div class="name">&nbsp;Bruschetta (6)</div><div>Tomatoes, basilic,,oignons, hulie d'olive<br>Tomatoes, basil, onions, olive oil &amp; garlic</div><span class="price">$8.50</span></div>
    <div class="item" style="top:96px"><div class="name">Bruschetta au tartare de saumon (4)</div><div>Tartare de saumon, tomates, basilic, oi-<br>gnons, hulie d'olive &amp; ail<br>Salmon tartar, tomatoes, basil, onions,<br>olive oil &amp; garlic</div><span class="price">$10.25</span></div>
    <div class="item" style="top:184px"><div class="name">Pain gratine / cheese bread</div><div>Rondelle d'oignion / onion ring<br>Soupe du jour / soup of the day<br>Soupe a l'oignon gratinee / onion soup<br>Crevettes a l'ail / garlic shrimp (6) <span style="text-transform:none">pieces</span></div>
      <span class="price">$7.50</span><span class="price" style="top:15px">$4.50</span><span class="price" style="top:29px">$3.95</span><span class="price" style="top:44px">$6.95</span><span class="price" style="top:58px">$8.95</span></div>

    <h2 class="section-title" style="left:3px;top:272px">SALADES REPAS</h2>

    <div class="item" style="top:302px"><div class="name">Salade ceasar / ceasar salad</div><div>Laitues, croutons, parmesan 7 vinaigrette<br>caesar maison<br>Lettuce, croutons, parmesan &amp; house<br>caesar dressing made with<br>anchovies &amp; capers</div><span class="price">$12.95</span></div>
    <div class="item" style="top:403px"><div class="name">Salade nicoise / nicoise salad</div><div>Haricots, pomme de terre, thon, tomates,<br>concombre, oeufs &amp; vinaigrette maison<br>Green beans, potatoes, tuna, tomatoes, cu-<br>cumbers, eggs house vinaigrette</div><span class="price">$15.95</span></div>
    <div class="item" style="top:490px"><div class="name">Salade fromage de chevre / goat cheese<br>salad</div><div>Laitues, , piments, fromage de chevres ,<br>tomate, concombre<br>Lettuce, , peppers, goeat cheese, tomato,<br>cucumbers</div><span class="price">$15.95</span></div>
    <div class="item" style="top:592px"><div class="name">Salade fruit de mer / seafood salad</div><div>Laitue, goberge, piments, mayonnaise &amp;<br>morceaux d'orange<br>Lettuce, peppers, peppers crab sticks &amp;<br>orange pieces</div><span class="price">$15.95</span></div>
    <div class="item" style="top:694px"><div class="name">Salade grecque / greek salad</div><div>Tomates, concombres, ognion rouge,<br>olives kalamata, fromage feta<br>Tomatoes, cucumbers, red onions, red pep-<br>pers, olives, feta</div><span class="price">$15.95</span></div>
    <div class="item" style="top:781px"><div class="name">Salade de saumon fume capres &amp; ognions</div><span class="price">$12.95</span></div>
  </div>
</section>

</body>
</html>
```